Business Card Design for a Lending Business (Hard Money loans)

We need a business card for our Real Estate Lending business. We do hard Money loans for real estate investors. We have an existing logo we like, see attached. I'd like the business card to mostly include the logo colors, but a bright color pop of some sort would be nice to see also. Card should include Logo, Company Name, Company Address, Employee Name, Cell Phone, Main Phone, Email, Website

Industry/Entity Type

Finance / Lending

Contact Information for Business Card

Logo, Company Name, Company Address, Employee Name, Cell Phone, Main Phone, Email, Website

Requirements
Nice to have
• I'd like the business card to mostly include the logo colors, but a bright color pop of some sort would be nice to see also.

```html
<!DOCTYPE html>
<html lang="en">
<head>
<meta charset="utf-8">
<title>Harbor Lane Lending – Business Card</title>
<link rel="stylesheet" href="https://fonts.googleapis.com/css2?family=Montserrat:wght@700;800&family=Open+Sans:wght@400;600&display=swap">
<style>
  :root {
    --stage: #232323;
    --navy: #283583;
    --navy-deep: #1f2a6e;
    --navy-soft: #33469a;
    --cyan: #12a9de;
    --cyan-dark: #0e87b8;
    --white: #ffffff;
  }
  * { box-sizing: border-box; margin: 0; padding: 0; }
  html, body { width: 1200px; height: 780px; overflow: hidden; background: var(--stage); }
  .canvas { position: relative; width: 1200px; height: 780px; }

  .card {
    position: absolute;
    width: 600px;
    height: 343px;
    overflow: hidden;
    box-shadow: 0 12px 30px rgba(0,0,0,.55);
  }
  .card--back { left: 110px; top: 32px; }
  .card--front { left: 490px; top: 405px; background: var(--navy); }

  /* back side */
  .back-pattern {
    position: absolute; inset: 0;
    background: linear-gradient(200deg, var(--navy-soft) 0%, var(--navy) 55%, var(--navy-deep) 100%);
  }
  .back-brand {
    position: absolute; right: 56px; top: 150px;
    display: flex; align-items: center; gap: 8px;
    font-family: "Montserrat", sans-serif; font-weight: 700;
    font-size: 12px; letter-spacing: 1.5px; text-transform: uppercase;
    color: var(--white);
  }
  .brand-dot { width: 14px; height: 14px; border-radius: 50%; background: var(--cyan); }

  /* front side */
  .front-shape { position: absolute; inset: 0; }

  .holder {
    position: absolute; left: 22px; top: 62px;
    padding-left: 18px;
    border-left: 12px solid var(--cyan);
  }
  .holder-name {
    font-family: "Montserrat", sans-serif; font-weight: 800;
    font-size: 28px; line-height: 1.05; color: var(--white);
  }
  .holder-name .first { color: var(--cyan); }
  .holder-title {
    font-family: "Open Sans", sans-serif; font-weight: 600;
    font-size: 15px; color: var(--white); margin-top: 4px;
  }

  .address {
    position: absolute; left: 52px; top: 178px;
    font-family: "Open Sans", sans-serif; font-size: 13.5px; line-height: 1.35;
    color: var(--white);
  }
  .contacts {
    position: absolute; left: 52px; top: 232px;
    list-style: none;
    font-family: "Open Sans", sans-serif; font-size: 13.5px; color: var(--white);
  }
  .contacts li { display: flex; align-items: center; gap: 9px; height: 22px; }
  .contacts svg { width: 14px; height: 14px; flex: none; }

  .front-brand {
    position: absolute; right: 34px; top: 118px;
    width: 190px;
    display: flex; flex-direction: column; align-items: center; gap: 12px;
    font-family: "Montserrat", sans-serif; font-weight: 700;
    font-size: 22px; letter-spacing: 3px; line-height: 1.2;
    text-transform: uppercase; text-align: center;
    color: var(--navy);
  }
  .front-brand .brand-dot { width: 46px; height: 46px; background: var(--navy); }
</style>
</head>
<body>
<main class="canvas">

  <section class="card card--back" aria-label="Card back">
    <div class="back-pattern" role="img" aria-label="Repeating brand monogram pattern in soft blue tones"></div>
    <div class="back-brand"><span class="brand-dot"></span>Harbor Lane Lending</div>
  </section>

  <section class="card card--front" aria-label="Card front">
    <svg class="front-shape" viewBox="0 0 600 343" width="600" height="343" aria-hidden="true">
      <path d="M392 0 Q300 250 458 343 L600 343 L600 0 Z" fill="var(--cyan)"/>
      <path d="M404 0 Q322 250 472 343 L600 343 L600 0 Z" fill="var(--cyan-dark)"/>
      <path d="M410 0 Q330 250 478 343 L600 343 L600 0 Z" fill="var(--white)"/>
    </svg>

    <div class="holder">
      <h1 class="holder-name"><span class="first">Marta</span> Velinova</h1>
      <p class="holder-title">Managing Director</p>
    </div>

    <address class="address">
      418 Alder Ridge Rd. Suite 310<br>
      Ashford, TX 75409
    </address>

    <ul class="contacts">
      <li>
        <svg viewBox="0 0 14 14" aria-label="Cell"><rect x="3.5" y="1" width="7" height="12" rx="1.5" fill="none" stroke="var(--cyan)" stroke-width="1.3"/></svg>
        (555) 214-3860
      </li>
      <li>
        <svg viewBox="0 0 14 14" aria-label="Main phone"><path d="M3 1.5 L5.3 1.5 L6.2 4.4 L4.8 5.6 Q6 8.2 8.4 9.4 L9.7 8 L12.5 9 L12.5 11.3 Q12.3 12.8 10.7 12.6 Q2.2 11.6 1.4 3.2 Q1.3 1.6 3 1.5 Z" fill="var(--cyan)"/></svg>
        (555) 214-3900
      </li>
      <li>
        <svg viewBox="0 0 14 14" aria-label="Email"><rect x="1" y="3" width="12" height="8.5" rx="1" fill="none" stroke="var(--cyan)" stroke-width="1.3"/><path d="M1.5 3.5 L7 8 L12.5 3.5" fill="none" stroke="var(--cyan)" stroke-width="1.3"/></svg>
        info@harborlanelending.com
      </li>
      <li>
        <svg viewBox="0 0 14 14" aria-label="Website"><circle cx="7" cy="7" r="5.8" fill="none" stroke="var(--cyan)" stroke-width="1.3"/><ellipse cx="7" cy="7" rx="2.5" ry="5.8" fill="none" stroke="var(--cyan)" stroke-width="1"/><line x1="1.2" y1="7" x2="12.8" y2="7" stroke="var(--cyan)" stroke-width="1"/></svg>
        www.harborlanelending.com
      </li>
    </ul>

    <div class="front-brand">
      <span class="brand-dot"></span>
      <span>Harbor Lane<br>Lending</span>
    </div>
  </section>

</main>
</body>
</html>
```